Cybersecurity Course - Bastion Trailplan: HOLV TPX Program

this is a graphic for a course I will launch. I have attached the ebook that will accompany the course. Logo also attached.

Size is 1280 x 720 pixels, with a minimum width of 640 pixels. The aspect ratio should be 16:9. The maximum file size is 2 MB.

Title: Bastion Trailplan: HOLV TPX Program
- MASTER Governance Risk Management & Compliance (GRC) with HOLV TPX 2.0
- Learn through real-world industry applications, examples, and samples
- Access downloadable HOLV TPX 2.0 resources and experience a guided walkthrough with a mentor

Target Market(s)

IT services

Industry/Entity Type

cybersecurity

Colors
0054AA
0677BA
7BADD7
CADEEF
E8F1F8

Requirements
Must have
• 1280 x 720 pixel

```html
<!DOCTYPE html>
<html lang="en">
<head>
<meta charset="utf-8">
<title>Bastion Trailplan: HOLV TPX Program</title>
<link rel="stylesheet" href="https://fonts.googleapis.com/css2?family=Crimson+Pro:wght@600;700&display=swap">
<style>
  :root {
    --navy-ink: #0b2a42;
    --navy-soft: #1d3f5e;
    --sky-top: #ffffff;
    --sky-mid: #cae6f8;
    --sky-bottom: #3db5f7;
    --shield-deep: #0677ba;
    --shield-light: #7badd7;
  }
  * { margin: 0; padding: 0; box-sizing: border-box; }
  html, body { width: 1200px; height: 675px; overflow: hidden; }
  body {
    font-family: "Crimson Pro", Georgia, serif;
    color: var(--navy-ink);
  }
  .course-banner {
    position: relative;
    width: 1200px;
    height: 675px;
    overflow: hidden;
    background: linear-gradient(180deg, var(--sky-top) 0%, var(--sky-top) 40%, var(--sky-mid) 62%, var(--sky-bottom) 100%);
  }
  .brand-name {
    position: absolute;
    left: 222px;
    top: 150px;
    width: 240px;
    text-align: center;
    font-size: 30px;
    font-weight: 700;
    letter-spacing: 2px;
    line-height: 1.05;
    color: var(--navy-ink);
  }
  .course-title {
    position: absolute;
    left: 66px;
    top: 278px;
    font-size: 60px;
    font-weight: 700;
    line-height: 1;
    letter-spacing: 0.5px;
    color: var(--navy-ink);
  }
  .course-subtitle {
    position: absolute;
    left: 67px;
    top: 352px;
    font-size: 52px;
    font-weight: 600;
    line-height: 1;
    color: var(--navy-soft);
  }
  .benefit-list {
    position: absolute;
    left: 86px;
    top: 418px;
    width: 620px;
    list-style: none;
  }
  .benefit-list li {
    position: relative;
    padding-left: 28px;
    margin-bottom: 12px;
    font-size: 23px;
    font-weight: 600;
    line-height: 27px;
    color: var(--navy-ink);
  }
  .benefit-list li::before {
    content: "";
    position: absolute;
    left: 0;
    top: 9px;
    width: 13px;
    height: 13px;
    background: var(--navy-ink);
  }
  .security-illustration {
    position: absolute;
    left: 737px;
    top: 60px;
    width: 370px;
    height: 550px;
  }
</style>
</head>
<body>
  <main class="course-banner">
    <div class="brand-name">VERADYN<br>ACADEMY</div>

    <h1 class="course-title">BASTION TRAILPLAN:</h1>
    <h2 class="course-subtitle">HOLV TPX Program</h2>

    <ul class="benefit-list">
      <li>MASTER Governance Risk Management &amp; Compliance (GRC) with HOLV TPX 2.0</li>
      <li>Learn through real-world industry applications, examples, and samples</li>
      <li>Access downloadable HOLV TPX 2.0 resources and experience a guided walkthrough with a mentor</li>
    </ul>

    <svg class="security-illustration" viewBox="0 0 370 550" role="img" aria-label="Illustration of a blue security shield with a padlock standing on a stacked platform">
      <defs>
        <linearGradient id="shieldTone" x1="0" y1="0" x2="0" y2="1">
          <stop offset="0" stop-color="var(--shield-deep)"/>
          <stop offset="1" stop-color="var(--shield-light)"/>
        </linearGradient>
      </defs>
      <rect x="0" y="0" width="370" height="550" rx="40" fill="url(#shieldTone)"/>
    </svg>
  </main>
</body>
</html>
```